Flyer Design Project

asphalt paving company needs 3 designs for inserts to place inside presentation folder. I will up load samples of basic concept and information required but needs to be completely redesigned. Looking for professional modern look.

Industry/Entity Type

It Company

```html
<!DOCTYPE html>
<html lang="en">
<head>
<meta charset="utf-8">
<title>Services</title>
<link rel="stylesheet" href="https://fonts.googleapis.com/css2?family=Arimo&family=Audiowide&display=swap">
<style>
  :root {
    --orange: #f7941d;
    --orange-deep: #e07a10;
    --peach: #fbd6a8;
    --ink: #1a1a1a;
    --title-outline: #2b1a08;
    --paper: #ffffff;
  }
  html, body { margin: 0; padding: 0; overflow: hidden; background: var(--paper); }
  .sheet {
    position: relative;
    width: 848px;
    height: 1200px;
    overflow: hidden;
    background: var(--paper);
    font-family: "Arimo", Arial, sans-serif;
    color: var(--ink);
  }
  .decor { position: absolute; inset: 0; }
  .title {
    position: absolute;
    left: 28px;
    top: 70px;
    margin: 0;
    font-family: "Audiowide", sans-serif;
    font-size: 96px;
    font-weight: 400;
    letter-spacing: 1px;
    line-height: 1;
    color: var(--orange);
    -webkit-text-stroke: 3px var(--title-outline);
    paint-order: stroke fill;
    text-shadow: 3px 3px 0 var(--title-outline);
    transform: scaleY(0.72);
    transform-origin: left top;
  }
  .service-item {
    position: absolute;
    font-size: 16.5px;
    line-height: 20px;
    white-space: nowrap;
  }
  .photo {
    position: absolute;
    box-sizing: border-box;
    border: 3px solid var(--orange);
    border-radius: 22px 4px 22px 4px;
    padding: 5px;
    background: var(--paper);
  }
  .photo-fill {
    width: 100%;
    height: 100%;
    border-radius: 16px 2px 16px 2px;
  }
  .photo-roller .photo-fill { background: linear-gradient(180deg, #b9d3ea 0%, #8fa7a0 38%, #3a3b3d 60%, #222 100%); }
  .photo-site .photo-fill { background: linear-gradient(180deg, #9fa3a2 0%, #7d8079 35%, #5b5347 65%, #45403a 100%); }
  .photo-striping .photo-fill { background: linear-gradient(180deg, #dfe6ee 0%, #c8ccd0 30%, #3b3c40 52%, #2a2b2e 100%); }
  .photo-milling .photo-fill { background: linear-gradient(160deg, #e8ecef 0%, #b8bcbd 40%, #7a7770 70%, #55524c 100%); }
</style>
</head>
<body>
<div class="sheet">
  <svg class="decor" width="848" height="1200" viewBox="0 0 848 1200" aria-hidden="true">
    <defs>
      <radialGradient id="dot-glow" cx="0.45" cy="0.35" r="0.6">
        <stop offset="0" stop-color="#f9b870" stop-opacity="0.75"/>
        <stop offset="0.6" stop-color="#fbd6a8" stop-opacity="0.35"/>
        <stop offset="1" stop-color="#ffffff" stop-opacity="0"/>
      </radialGradient>
      <linearGradient id="road" x1="0" y1="0" x2="0" y2="1">
        <stop offset="0" stop-color="#f2b15a"/>
        <stop offset="0.3" stop-color="#c8741e"/>
        <stop offset="1" stop-color="#6b3608"/>
      </linearGradient>
      <linearGradient id="line-wash" x1="0" y1="1" x2="1" y2="0">
        <stop offset="0" stop-color="#f9c98c" stop-opacity="0.05"/>
        <stop offset="0.5" stop-color="#f7b46a" stop-opacity="0.35"/>
        <stop offset="1" stop-color="#f9c98c" stop-opacity="0.1"/>
      </linearGradient>
    </defs>

    <!-- soft orange field behind the title -->
    <ellipse cx="380" cy="230" rx="420" ry="200" fill="url(#dot-glow)"/>

    <!-- curved road banner -->
    <path role="img" aria-label="Photo of an open highway stretching to the horizon in warm orange light"
          d="M295,0 C325,110 440,165 560,175 C700,185 805,230 848,335 L848,0 Z" fill="url(#road)"/>

    <!-- soft line wash, lower right -->
    <path d="M250,1200 C420,1080 560,880 848,640 L848,760 C640,930 520,1080 440,1200 Z" fill="url(#line-wash)"/>
    <path d="M560,560 C680,600 780,640 848,700 L848,730 C770,680 680,640 560,580 Z" fill="url(#line-wash)"/>

    <g fill="none" stroke="#f7941d" stroke-width="1.6" stroke-dasharray="2 2">
      <!-- group one -->
      <path d="M82,320 V488 H505"/>
      <path d="M82,320 H104 M82,361 H104 M82,402 H104 M82,444 H104"/>
      <path d="M293,318 V488"/>
      <path d="M293,318 H318 M293,360 H318 M293,402 H318 M293,444 H318"/>
      <!-- group two -->
      <path d="M345,700 H465 V530"/>
      <path d="M465,530 H490 M465,571 H490 M465,612 H490 M465,655 H490 M465,698 H490"/>
      <!-- group three -->
      <path d="M82,758 V930 H503"/>
      <path d="M82,758 H104 M82,800 H104 M82,842 H104 M82,883 H104"/>
      <!-- group four -->
      <path d="M342,1140 H482 V959"/>
      <path d="M482,959 H506 M482,995 H506 M482,1031 H506 M482,1067 H506 M482,1103 H506"/>
    </g>
  </svg>

  <h1 class="title">SERVICES</h1>

  <!-- paving -->
  <div class="service-item" style="left:108px;top:310px">New Grade/Pave</div>
  <div class="service-item" style="left:108px;top:351px">Remove &amp; Replace</div>
  <div class="service-item" style="left:108px;top:392px">Fabric Overlays</div>
  <div class="service-item" style="left:108px;top:434px">Skin Patching</div>
  <div class="service-item" style="left:324px;top:308px">Seal Coating</div>
  <div class="service-item" style="left:324px;top:350px">Road Slurry</div>
  <div class="service-item" style="left:324px;top:392px">Trench Repairs</div>
  <div class="service-item" style="left:324px;top:434px">Crack Seal</div>
  <div class="photo photo-roller" style="left:505px;top:303px;width:263px;height:185px">
    <div class="photo-fill" role="img" aria-label="Asphalt roller compacting a freshly paved parking lot"></div>
  </div>

  <!-- concrete -->
  <div class="photo photo-site" style="left:80px;top:517px;width:265px;height:183px">
    <div class="photo-fill" role="img" aria-label="Crew preparing a graded concrete slab site"></div>
  </div>
  <div class="service-item" style="left:496px;top:520px">Concrete</div>
  <div class="service-item" style="left:496px;top:561px">Truncated Domes</div>
  <div class="service-item" style="left:496px;top:602px">Curbs</div>
  <div class="service-item" style="left:496px;top:645px">Gutters</div>
  <div class="service-item" style="left:496px;top:688px">Slabs</div>

  <!-- striping and access -->
  <div class="service-item" style="left:108px;top:748px">Striping/Signage</div>
  <div class="service-item" style="left:108px;top:790px">ADA Upgrades</div>
  <div class="service-item" style="left:108px;top:832px">ADA Ramps</div>
  <div class="service-item" style="left:108px;top:873px">ADA Rails</div>
  <div class="photo photo-striping" style="left:503px;top:745px;width:265px;height:183px">
    <div class="photo-fill" role="img" aria-label="Freshly striped crosswalk and stop marking in front of a shopping center"></div>
  </div>

  <!-- project support -->
  <div class="photo photo-milling" style="left:80px;top:955px;width:262px;height:185px">
    <div class="photo-fill" role="img" aria-label="Milling machine and loader grinding an old road surface"></div>
  </div>
  <div class="service-item" style="left:511px;top:949px">Free Estimates</div>
  <div class="service-item" style="left:511px;top:985px">Permit Applications</div>
  <div class="service-item" style="left:511px;top:1021px">Construction Management</div>
  <div class="service-item" style="left:511px;top:1057px">Design</div>
  <div class="service-item" style="left:511px;top:1093px">Import &amp; Export</div>
  <div class="service-item" style="left:511px;top:1129px">Demolition</div>
</div>
</body>
</html>
```